Bellweather Business Card & Letterhead
Business Card & Letterhead Design
I need single sided standard sized Business Card [3.5" x 2"]
Use whatever font you think looks best
Simple
Lorena Fitchett
71 Pellham Lane
Marietta, Georgia 30008
lorena@bellweatherpartners.example
www.bellweatherpartners.example

```html
<!DOCTYPE html>
<html lang="en">
<head>
<meta charset="utf-8">
<title>Bellweather Stationery</title>
<link href="https://fonts.googleapis.com/css2?family=Libre+Baskerville&family=Open+Sans:wght@400;600&display=swap" rel="stylesheet">
<style>
  :root {
    --backdrop: #ebe6df;
    --paper: #ffffff;
    --brand-blue: #1f6fc1;
    --brand-navy: #17407a;
    --ink: #4a4f57;
    --muted: #9aa1aa;
    --flap-dark: #5d6166;
    --flap-light: #9a9ea3;
    --shadow: rgba(60, 45, 30, 0.18);
  }
  * { margin: 0; padding: 0; box-sizing: border-box; }
  html, body { width: 1200px; height: 446px; overflow: hidden; }
  body {
    position: relative;
    background: var(--backdrop);
    font-family: "Open Sans", Arial, sans-serif;
    color: var(--ink);
  }
  .piece {
    position: absolute;
    background: var(--paper);
    box-shadow: 0 2px 6px var(--shadow);
    overflow: hidden;
  }
  .label {
    position: absolute;
    font-size: 8px;
    letter-spacing: 1.2px;
    text-transform: uppercase;
    color: #7c746a;
  }
  .brand {
    display: flex;
    align-items: center;
    gap: 5px;
    position: absolute;
  }
  .brand-square { background: var(--brand-blue); flex: none; }
  .brand-name {
    font-family: "Libre Baskerville", Georgia, serif;
    color: var(--brand-navy);
    text-transform: uppercase;
    letter-spacing: 0.5px;
    line-height: 1;
  }
  .brand-sub {
    font-size: 5px;
    letter-spacing: 2px;
    color: var(--muted);
    text-transform: uppercase;
    margin-top: 2px;
  }
  .stripe { position: absolute; left: 0; right: 0; background: var(--brand-blue); }

  /* business cards */
  .card { left: 19px; width: 132px; height: 76px; }
  .card-front { top: 211px; }
  .card-back { top: 332px; }
  .card .stripe { bottom: 0; height: 6px; }
  .card-contact {
    position: absolute;
    right: 8px; top: 30px;
    text-align: right;
    font-size: 4.3px;
    line-height: 1.45;
  }
  .card-contact .person { font-weight: 600; color: var(--brand-navy); font-size: 5.5px; }

  /* letterheads */
  .letterhead { top: 14px; width: 298px; height: 388px; }
  .letterhead-one { left: 163px; }
  .letterhead-two { left: 475px; }
  .letterhead .stripe { bottom: 8px; height: 5px; }
  .letterhead-footer {
    position: absolute;
    left: 14px; bottom: 17px;
    font-size: 4.5px;
    color: var(--muted);
    letter-spacing: 0.4px;
  }

  /* envelopes */
  .envelope-flap-band { left: 833px; top: 14px; width: 357px; height: 54px; background: var(--brand-blue); }
  .envelope-back { left: 833px; top: 82px; width: 357px; height: 152px; }
  .envelope-back svg { position: absolute; left: 0; top: 0; }
  .envelope-seal { position: absolute; left: 172px; top: 108px; width: 13px; height: 13px; background: var(--brand-blue); }
  .envelope-front { left: 799px; top: 288px; width: 387px; height: 137px; }
  .envelope-front .stripe { bottom: 6px; height: 5px; }
</style>
</head>
<body>

  <p class="label" style="left:19px; top:178px;">Stationery Elements</p>

  <section class="piece card card-front">
    <div class="brand" style="left:8px; top:8px;">
      <span class="brand-square" style="width:9px;height:9px;"></span>
      <div>
        <div class="brand-name" style="font-size:9px;">Bellweather</div>
        <div class="brand-sub" style="font-size:3.5px;">Partners</div>
      </div>
    </div>
    <div class="card-contact">
      <div class="person">Lorena Fitchett</div>
      <div>Managing Partner</div>
      <div>71 Pellham Lane, Marietta, Georgia 30008</div>
      <div>(770) 555-0142 · lbfitchett</div>
      <div>lorena@bellweatherpartners.example</div>
      <div>www.bellweatherpartners.example</div>
    </div>
    <div class="stripe"></div>
  </section>
  <p class="label" style="left:19px; top:296px;">Business Card Front</p>

  <section class="piece card card-back">
    <div class="brand" style="left:10px; top:28px;">
      <span class="brand-square" style="width:11px;height:11px;"></span>
      <div>
        <div class="brand-name" style="font-size:11px;">Bellweather</div>
        <div class="brand-sub" style="font-size:4px;">Partners</div>
      </div>
    </div>
    <div class="stripe"></div>
  </section>
  <p class="label" style="left:19px; top:416px;">Business Card Back</p>

  <section class="piece letterhead letterhead-one">
    <div class="brand" style="left:14px; top:14px;">
      <span class="brand-square" style="width:11px;height:11px;"></span>
      <div>
        <div class="brand-name" style="font-size:12px;">Bellweather</div>
        <div class="brand-sub">Partners</div>
      </div>
    </div>
    <p class="letterhead-footer">71 Pellham Lane · Marietta, Georgia 30008 · www.bellweatherpartners.example</p>
    <div class="stripe"></div>
  </section>
  <p class="label" style="left:250px; top:410px;">Letterhead Option 1</p>

  <section class="piece letterhead letterhead-two">
    <div class="brand" style="left:14px; top:14px;">
      <span class="brand-square" style="width:11px;height:11px;"></span>
      <div>
        <div class="brand-name" style="font-size:12px;">Bellweather</div>
        <div class="brand-sub">Partners</div>
      </div>
    </div>
    <p class="letterhead-footer">71 Pellham Lane · Marietta, Georgia 30008 · www.bellweatherpartners.example</p>
    <div class="stripe"></div>
  </section>
  <p class="label" style="left:562px; top:410px;">Letterhead Option 2</p>

  <div class="piece envelope-flap-band"></div>
  <section class="piece envelope-back">
    <svg width="357" height="152" viewBox="0 0 357 152" aria-hidden="true">
      <defs>
        <linearGradient id="flapShade" x1="0" y1="0" x2="0" y2="1">
          <stop offset="0" stop-color="var(--flap-dark)"/>
          <stop offset="1" stop-color="var(--flap-light)"/>
        </linearGradient>
      </defs>
      <path d="M0 0 H357 V18 Q357 40 330 48 L200 70 Q178 74 157 70 L27 48 Q0 40 0 18 Z" fill="url(#flapShade)"/>
      <path d="M0 70 L150 110 M357 70 L207 110" stroke="#e3e5e8" stroke-width="1" fill="none"/>
    </svg>
    <span class="envelope-seal"></span>
  </section>
  <p class="label" style="left:905px; top:244px;">Envelope Option 3</p>

  <section class="piece envelope-front">
    <div class="brand" style="left:14px; top:14px;">
      <span class="brand-square" style="width:10px;height:10px;"></span>
      <div>
        <div class="brand-name" style="font-size:11px;">Bellweather</div>
        <div class="brand-sub">Partners</div>
      </div>
    </div>
    <div class="stripe"></div>
  </section>

</body>
</html>
```